Financial Advisor Website Design

We are working with Kelvaro. They are a financial advising company that needs a new website design.

Some sites to use for inspiration:

https://investor.quillmarsh.com
https://www.hollisbrant.com/us-en
https://www.corvantel.com
https://www.aboutpellgrew.com

Thank you for taking the time to consider designing a website for us. We are web developers based in Stockton and Los Angeles, CA, USA. Most of our projects go through the same process. Understanding this process may help you win a project with us. We custom-code all of our websites in-house. We don’t have any requirements as to what tools you use for your design, but we prefer Figma files. For any design that we label as four-stars, we send it to the client for review. The client picks the final design they want us to use. Once we complete this process, we will continue to show additional clients all the four-star sites and purchase them later. Your designs will have multiple chances to sell. For better chances of success, we ask that you follow these guidelines.

IMAGES:
If you use any images or icons in the design, we ask that you have a link to the asset so we can purchase the image/icon. Most of the designs we submit do not have the customer’s images on them unless they have some great images. Be creative; show us the feeling you are trying to portray with your image choices. Use any royalty-free site you choose. We subscribe to Parvel and mainly use their images, but we can purchase images outside of Parvel.

PLEASE NOTE: we will not submit designs to clients with watermarks on the images.

FONTS:
We ask that you identify the fonts used in the design. This can be done in a message if you want. We typically use Tessly Fonts and Parvel Fonts.

CONTENT:
We're always open to different content and ideas. We often submit designs with stock images so the client can see our vision. We typically take pictures after the website launch to use their images with our vision. Lorem Ipsum is fine for paragraphs, but we ask that you write the headers in correct English. We want to be able to show the vision and identify the sections of the website.

INSPIRATION:
We typically add a couple of links in the brief of websites we like to help you get started in your design.

REVISIONS:
We do not often ask for revisions of the designs unless we see something in the design that may not appeal to the client. If there are slight changes that we want to make, we do that in the development process.

FEEDBACK:
We rarely give feedback on designs during the design process. We are working on many website projects and do not have the time to provide feedback. We usually respond if your request is well thought out and asks specific questions, but a note asking “feedback, please” usually goes unanswered.

```html
<!DOCTYPE html>
<html lang="en">
<head>
<meta charset="UTF-8">
<title>Kelvaro — Website Design</title>
<link href="https://fonts.googleapis.com/css2?family=Instrument+Sans:wght@400;500;600;700&display=swap" rel="stylesheet">
<style>
:root{
  --yellow:#f1d854;
  --navy:#072649;
  --blue:#0d3968;
  --mist:#e4eaf0;
  --paper:#f7f8f9;
  --stage:#d0d0d0;
  --ink:#072649;
  --muted:#5b6675;
  --line:#dfe4ea;
}
*{box-sizing:border-box;margin:0;padding:0}
html,body{width:1200px;height:3660px;overflow:hidden}
body{background:var(--stage);font-family:"Instrument Sans",sans-serif;color:var(--ink);position:relative}
.abs{position:absolute}

/* wordmark: plain name, one colour, one weight */
.wordmark{display:flex;align-items:center;gap:6px;font-weight:600;color:var(--navy);letter-spacing:0}
.wordmark i{display:block;border-radius:50%;background:var(--yellow)}

/* style guide */
.guide-logo{left:224px;top:132px;font-size:26px}
.guide-logo i{width:14px;height:14px}
.guide-title{font-size:22px;font-weight:500;color:var(--navy)}
.guide-fonts{left:486px;top:96px}
.guide-fontname{left:486px;top:138px;font-size:17px;color:#3b4a5c}
.guide-colors{left:733px;top:96px}
.swatches{left:733px;top:132px;display:flex;gap:9px}
.swatch{width:40px;text-align:center;font-size:9px;color:#444}
.swatch i{display:block;width:40px;height:40px;border-radius:50%;margin-bottom:8px}

/* site */
.site{left:245px;top:256px;width:709px;height:3299px;background:#fff;overflow:hidden}
.site .abs{position:absolute}
.btn{display:inline-block;background:var(--yellow);color:var(--navy);font-size:7.5px;font-weight:600;padding:7px 10px;border-radius:2px}
.link{display:inline-block;font-size:7.5px;font-weight:600;color:var(--navy);border-bottom:1.5px solid var(--yellow);padding-bottom:2px}
.link.light{color:#fff}
h2{font-weight:500;font-size:22px;line-height:1.22;color:var(--navy);letter-spacing:-.2px}
p.body{font-size:7.5px;line-height:1.65;color:#3d4a5a}

.topbar{top:0;left:0;width:709px;height:36px;border-bottom:1px solid var(--line)}
.brand{left:66px;top:11px;font-size:12px}
.brand i{width:7px;height:7px}
.portal{left:146px;top:15px;font-size:6px;color:var(--blue);border-left:1px solid var(--line);padding-left:8px}
.util{right:66px;top:15px;font-size:6px;color:var(--blue);display:flex;gap:14px}
.nav{top:36px;left:66px;width:576px;height:34px;display:flex;align-items:center;gap:19px;font-size:6px;color:#5b6675}
.contact{position:absolute;right:0;top:8px;border:1px solid var(--yellow);font-size:6px;padding:5px 13px;border-radius:2px;color:var(--navy)}

.hero{top:70px;left:0;width:709px;height:354px;overflow:hidden;background:linear-gradient(180deg,#0b2f5c 0%,#1d4a7a 45%,#7d95ad 75%,#c9d3dc 100%)}
.hero-sun{right:-98px;top:-98px;width:284px;height:284px;border-radius:50%;background:var(--yellow)}
.hero-hikers{left:460px;top:60px;width:190px;height:294px;background:linear-gradient(180deg,rgba(200,150,40,.45),rgba(30,40,60,.6));border-radius:40% 40% 0 0}
.hero-copy{left:66px;top:44px;width:300px;color:#fff}
.hero-copy h1{font-size:30px;font-weight:600;line-height:1.05;letter-spacing:-.5px}
.hero-copy p{font-size:9px;line-height:1.45;margin:22px 0 26px}

.intro{top:424px;left:0;width:709px;height:165px;background:var(--paper)}
.intro h2{left:66px;top:40px;width:280px}
.intro .side{left:412px;top:40px;width:230px}

.power-img{top:633px;left:66px;width:289px;height:190px;background:linear-gradient(135deg,#d9c29a,#e6c24c 55%,#6f7f95)}
.power{top:670px;left:411px;width:231px}
.checks{display:grid;grid-template-columns:1fr .8fr 1fr;row-gap:11px;margin-top:14px;font-size:6.5px;font-weight:500;color:var(--blue)}
.checks span::before{content:"✓";color:var(--yellow);margin-right:4px;font-weight:700}

.invest{top:880px;left:66px;width:300px}
.invest p{margin:14px 0 30px}
.list{top:874px;left:411px;width:231px}
.list div{height:29px;border-bottom:1px solid var(--line);display:flex;justify-content:space-between;align-items:center;font-size:6.5px;color:#6b7684}

.help-h{top:1103px;left:66px}
.band{top:1179px;left:0;width:709px;height:365px;background:var(--navy)}
.card{top:1149px;width:180px;color:#fff}
.card .ph{height:256px}
.card h3{font-size:11.5px;font-weight:600;margin:16px 0 7px}
.card p{font-size:7px;line-height:1.6;color:#c8d2de;width:172px}
.more{display:flex;align-items:center;gap:5px;font-size:7px;font-weight:600;color:var(--yellow);margin-top:13px}
.more b{width:15px;height:15px;border-radius:50%;background:var(--yellow);display:flex;align-items:center;justify-content:center}

.sol-h{top:1589px;left:0;width:709px;text-align:center}
.tabs{top:1636px;left:66px;width:576px;display:flex;justify-content:space-around;font-size:7px;color:#6b7684;border-bottom:1px solid var(--line);padding-bottom:7px}
.tabs .on{color:var(--navy);font-weight:500;border-bottom:2px solid var(--yellow);padding-bottom:5px;margin-bottom:-9px}
.sol-card{top:1675px;left:66px;width:576px;height:191px;border:1px solid var(--line);display:flex}
.sol-card .txt{width:286px;padding:32px 26px}
.sol-card h3{font-size:15px;font-weight:500;margin-bottom:14px}
.sol-card .ph{flex:1;background:linear-gradient(135deg,#e9ecef,#b8c4d2 55%,#2e4d78)}

.why{top:1910px;left:0;width:709px;height:251px;background:var(--paper)}
.why h2{position:absolute;top:42px;width:709px;text-align:center}
.quote{position:absolute;left:135px;top:98px;width:310px}
.quote p{font-size:17px;line-height:1.25;color:var(--navy)}
.quote .rule{height:1px;background:var(--line);margin:18px 0 16px;width:310px}
.quote b{font-size:7.5px;font-weight:600;display:block}
.quote small{font-size:6.5px;color:#6b7684}
.avatar{position:absolute;left:478px;top:97px;width:96px;height:96px;border-radius:50%;background:linear-gradient(135deg,#dfe6ee,#8b9bb0)}
.qmark{position:absolute;left:473px;top:162px}

.res-h{top:2204px;left:66px}
.res-main{top:2248px;left:66px;width:299px;height:188px;background:linear-gradient(135deg,#eef0f2,#c9cdd3 60%,#e2b437)}
.res-lead{top:2270px;left:399px;width:260px}
.meta{font-size:5.5px;color:#6b7684;margin-bottom:6px}
.res-lead h3{font-size:21px;font-weight:500;line-height:1.2;margin-bottom:12px}
.res-item{width:290px;display:flex;gap:12px}
.res-item .ph{width:100px;height:77px;flex:none}
.res-item h4{font-size:12px;font-weight:500;line-height:1.3;margin-bottom:4px}
.res-item .more{color:var(--navy);margin-top:8px}
.res-all{top:2669px;left:66px}

.cta{top:2720px;left:0;width:709px;height:327px;background:var(--navy)}
.cta h2{position:absolute;left:66px;top:104px;width:290px;color:#fff}
.cta p{position:absolute;left:66px;top:170px;width:280px;color:#c8d2de}
.cta .acts{position:absolute;left:66px;top:218px;display:flex;gap:9px;align-items:center}
.c1{left:418px;top:45px;width:100px;height:100px;border-radius:50%;background:linear-gradient(135deg,#f1e3c2,#d7b37a)}
.c2{left:433px;top:90px;width:209px;height:209px;border-radius:50%;background:linear-gradient(135deg,#eef1f5,#9fb2c9 60%,#5678a0)}
.dot{left:423px;top:129px;width:36px;height:36px;border-radius:50%;background:var(--yellow)}

.footer{top:3047px;left:66px;width:576px;height:252px}
.cols{position:absolute;top:47px;left:0;width:576px;display:flex}
.col{font-size:5.8px;color:#6b7684;line-height:2.9}
.col b{color:var(--navy);font-weight:600;display:block}
.flogo{position:absolute;left:0;top:174px;font-size:11px}
.flogo i{width:6px;height:6px}
.copy{position:absolute;right:0;top:178px;font-size:5px;color:#6b7684}
</style>
</head>
<body>

<div class="abs wordmark guide-logo">Kelvaro<i></i></div>
<div class="abs guide-title guide-fonts">Fonts:</div>
<div class="abs guide-fontname">Instrument Sans</div>
<div class="abs guide-title guide-colors">Colors:</div>
<div class="abs swatches">
  <div class="swatch"><i style="background:#f1d854"></i>#f1d854</div>
  <div class="swatch"><i style="background:#072649"></i>#072649</div>
  <div class="swatch"><i style="background:#0d3968"></i>#0d3968</div>
  <div class="swatch"><i style="background:#e4eaf0"></i>#e4eaf0</div>
  <div class="swatch"><i style="background:#f7f8f9"></i>#f7f8f9</div>
</div>

<main class="abs site">
  <header class="abs topbar">
    <div class="abs wordmark brand">Kelvaro<i></i></div>
    <div class="abs portal">Investor Portal Login</div>
    <div class="abs util"><span>EN ◦</span><span>Search ◦</span></div>
  </header>
  <nav class="abs nav">
    <span>Products &amp; Services</span><span>Portfolio</span><span>Resources</span><span>Insights</span><span>Why Kelvaro</span>
    <span class="contact">Contact Us</span>
  </nav>

  <section class="abs hero" role="img" aria-label="Snowy mountain range under a deep blue sky">
    <div class="abs hero-sun"></div>
    <div class="abs hero-hikers" role="img" aria-label="Parent and child hiking up a rocky mountain ridge"></div>
    <div class="abs hero-copy">
      <h1>Your guide to every financial summit.</h1>
      <p>Through every twist and turn, we help you navigate your path with confidence.</p>
      <span class="btn">Find an Advisor</span>
    </div>
  </section>

  <section class="abs intro">
    <h2 class="abs">Invest in what matters. Everything worth having is worth investing in.</h2>
    <div class="abs side">
      <p class="body">Smart investing isn't just about money—it's about dedicating your resources to what truly matters. At Kelvaro Financial, we help you focus on what's worth your time.</p>
      <div style="margin-top:12px;display:flex;gap:9px;align-items:center"><span class="btn">Become an Investor</span><span class="link">Talk to an Expert</span></div>
    </div>
  </section>

  <div class="abs power-img" role="img" aria-label="Smiling family of three hugging at home"></div>
  <div class="abs power">
    <h2>Powering possibilities</h2>
    <p class="body" style="margin-top:10px">Near or far, our global reach helps you find the perfect fit for optimal cost efficiency and agility.</p>
    <div class="checks"><span>Health Solutions</span><span>Health</span><span>Health Solutions</span><span>Health Solutions</span><span>Health</span><span>Health Solutions</span></div>
  </div>

  <div class="abs invest">
    <h2>Investment to support your financial strategy</h2>
    <p class="body">We offer a wide range of options to build your portfolio.</p>
    <div style="display:flex;gap:9px;align-items:center"><span class="btn">Become an Investor</span><span class="link">Talk to an Expert</span></div>
  </div>
  <div class="abs list">
    <div>Investment Strategies<span>›</span></div>
    <div>Cash Flow<span>›</span></div>
    <div>Market Changes<span>›</span></div>
    <div>Personal Loans<span>›</span></div>
    <div>Mutual Funds<span>›</span></div>
    <div>Money market funds<span>›</span></div>
  </div>

  <h2 class="abs help-h">How can we help you?</h2>
  <div class="abs band"></div>
  <article class="abs card" style="left:66px">
    <div class="ph" role="img" aria-label="Older couple embracing and smiling" style="background:linear-gradient(160deg,#e9e3d6,#d9b84a 70%,#8a7a5a)"></div>
    <h3>Prep for retirement</h3>
    <p>Work with an advisor or a robo-advisor to get a personalized strategy in place.</p>
    <div class="more">LEARN MORE <b><svg width="6" height="6" viewBox="0 0 6 6"><path d="M2 1l2 2-2 2" stroke="#072649" fill="none"/></svg></b></div>
  </article>
  <article class="abs card" style="left:264px">
    <div class="ph" role="img" aria-label="Woman standing by a window in a bright empty room" style="background:linear-gradient(180deg,#eef0f1,#cfd4d8 60%,#b9a88a)"></div>
    <h3>Real estate planning</h3>
    <p>Work with an advisor or a robo-advisor to get a personalized strategy in place.</p>
    <div class="more">LEARN MORE <b><svg width="6" height="6" viewBox="0 0 6 6"><path d="M2 1l2 2-2 2" stroke="#072649" fill="none"/></svg></b></div>
  </article>
  <article class="abs card" style="left:462px">
    <div class="ph" role="img" aria-label="Advisor shaking hands with a smiling couple" style="background:linear-gradient(160deg,#d8cfc0,#d9bd55 55%,#6c7a8c)"></div>
    <h3>Find financial advisor</h3>
    <p>Work with an advisor or a robo-advisor to get a personalized strategy in place.</p>
    <div class="more">LEARN MORE <b><svg width="6" height="6" viewBox="0 0 6 6"><path d="M2 1l2 2-2 2" stroke="#072649" fill="none"/></svg></b></div>
  </article>

  <h2 class="abs sol-h">Solutions for every situation</h2>
  <div class="abs tabs"><span class="on">Life and Health Risk</span><span>Financial Solutions</span><span>Retirement Claims</span><span>View All</span></div>
  <div class="abs sol-card">
    <div class="txt">
      <h3>Life and Health Risk</h3>
      <p class="body">A partner with financial strength, global reach, and local insight to help you manage change</p>
      <div class="checks"><span>Health Solutions</span><span>Health</span><span>Health Solutions</span><span>Health Solutions</span><span>Health</span><span>Health Solutions</span></div>
    </div>
    <div class="ph" role="img" aria-label="Smiling man with glasses in a blue blazer"></div>
  </div>

  <section class="abs why">
    <h2>Why partner with us?</h2>
    <div class="quote">
      <p>Their financial guidance helped me secure my family's future and manage life and health risks with confidence.</p>
      <div class="rule"></div>
      <b>Dale Ormsby</b><small>Partner</small>
    </div>
    <div class="avatar" role="img" aria-label="Portrait of a client in a suit"></div>
    <svg class="qmark" width="26" height="16" viewBox="0 0 26 16"><circle cx="7" cy="8" r="7" fill="#f1d854"/><circle cx="19" cy="8" r="7" fill="#f1d854"/></svg>
  </section>

  <h2 class="abs res-h">Helpful resources</h2>
  <div class="abs res-main" role="img" aria-label="Hand holding a phone beside a laptop"></div>
  <div class="abs res-lead">
    <div class="meta">2 MIN READ | BY KELVARO</div>
    <h3>Transition from “working for money” to “money working for you</h3>
    <p class="body">Near or far, our global reach helps you find the perfect fit for optimal cost efficiency and agility.</p>
    <div class="more" style="color:var(--navy)">LEARN MORE <b><svg width="6" height="6" viewBox="0 0 6 6"><path d="M2 1l2 2-2 2" stroke="#072649" fill="none"/></svg></b></div>
  </div>
  <div class="abs res-item" style="top:2463px;left:66px">
    <div class="ph" role="img" aria-label="Adult child hugging an aging parent" style="background:linear-gradient(135deg,#a9b9cc,#5f7590)"></div>
    <div><div class="meta">2 MIN READ | BY KELVARO</div><h4>How to help your aging parents with their finance</h4><div class="more">LEARN MORE <b><svg width="6" height="6" viewBox="0 0 6 6"><path d="M2 1l2 2-2 2" stroke="#072649" fill="none"/></svg></b></div></div>
  </div>
  <div class="abs res-item" style="top:2463px;left:365px">
    <div class="ph" role="img" aria-label="Couple reviewing paperwork together" style="background:linear-gradient(135deg,#c7d0da,#3e5878)"></div>
    <div><div class="meta">2 MIN READ | BY KELVARO</div><h4>How being married affects your money</h4><div class="more">LEARN MORE <b><svg width="6" height="6" viewBox="0 0 6 6"><path d="M2 1l2 2-2 2" stroke="#072649" fill="none"/></svg></b></div></div>
  </div>
  <div class="abs res-item" style="top:2562px;left:66px">
    <div class="ph" role="img" aria-label="Budget charts and a pen on a desk" style="background:linear-gradient(135deg,#dfe4ea,#1e3556 60%,#e0b84a)"></div>
    <div><div class="meta">2 MIN READ | BY KELVARO</div><h4>How to use a budget review to jump-start</h4><div class="more">LEARN MORE <b><svg width="6" height="6" viewBox="0 0 6 6"><path d="M2 1l2 2-2 2" stroke="#072649" fill="none"/></svg></b></div></div>
  </div>
  <div class="abs res-item" style="top:2562px;left:365px">
    <div class="ph" role="img" aria-label="Person working on a laptop at a table" style="background:linear-gradient(135deg,#ece8e1,#b6a58c)"></div>
    <div><div class="meta">2 MIN READ | BY KELVARO</div><h4>Two ways to protect your growing income</h4><div class="more">LEARN MORE <b><svg width="6" height="6" viewBox="0 0 6 6"><path d="M2 1l2 2-2 2" stroke="#072649" fill="none"/></svg></b></div></div>
  </div>
  <span class="abs link res-all">View All Resources</span>

  <section class="abs cta">
    <h2>Let's find what's right and needed for you.</h2>
    <p class="body" style="color:#c8d2de">Whether you're looking to maximize cash flow or pursue growth opportunities, we're excited to take on your business challenges.</p>
    <div class="acts"><span class="btn">Become an Investor</span><span class="link light">Talk to an Expert</span></div>
    <div class="abs c2" role="img" aria-label="Hands reviewing financial charts on paper and a laptop"></div>
    <div class="abs c1" role="img" aria-label="Family walking together on a beach"></div>
    <div class="abs dot"></div>
  </section>

  <footer class="abs footer">
    <div class="cols">
      <div class="col" style="width:113px"><b>Company</b>About<br>Team<br>Careers</div>
      <div class="col" style="width:143px"><b>Solutions</b>Retirement Plan<br>School Savings<br>Real Estate Planning<br>School Savings<br>Real Estate Planning</div>
      <div class="col" style="width:115px"><b>Resources</b>Press<br>Articles<br>Media</div>
      <div class="col" style="width:122px"><b>Support</b>FAQs<br>Contact<br>Help</div>
      <div class="col"><b><span style="color:var(--yellow)">●</span> Investor Portal Login</b></div>
    </div>
    <div class="wordmark flogo">Kelvaro<i></i></div>
    <div class="copy">Copyright © 2025 Kelvaro - All Rights Reserved | Privacy Policy | Terms</div>
  </footer>
</main>
</body>
</html>
```